Need simple and modern looking business card with all my information on one side and logo on the other side
Info :
Company name - VELMAR CONSTRUCTION LLC
Company addres- 418 harbor 87th. Dunmoor park ny 10352
Email- velmarllc@tridomail.Com
Company phone number 555-318-6094
Cell number- 555-742-0583
Web site - velmarllc.Com
My name Gerald tomasino

Target Market(s)

Construction , home improvement, remodeling

Industry/Entity Type

Construction

Contact Information for Business Card

It has to be moder but at the same time simple

Font styles to use
Sans Serif

Colors
0255a3
ffffff
000000
f78f20
b1b1b1
9d9d9d
1b1b1b
33a6d7
ec1f27

Requirements
Must have
• My logo on one side maybe with a some kind of background on the other side all my information
Nice to have
• Some kind of background pictures provided by you .PLEASE HAVE ACCOUNT WITH PIXELVAULT WILL NOT PAY ANY EXTRA FEES .
Should not have
• Any kind of hamer, nails,screws, helmets itp. Please do not copy the other designs come up with something new.

```html
<!DOCTYPE html>
<html lang="en">
<head>
<meta charset="utf-8">
<title>Velmar Construction LLC – Business Card</title>
<link href="https://fonts.googleapis.com/css2?family=Quicksand:wght@400;500;700&display=swap" rel="stylesheet">
<style>
  :root {
    --orange: #f78f20;
    --orange-light: #f9a630;
    --ink: #1b1b1b;
    --ink-soft: #2e2e2e;
    --blue: #0255a3;
    --red: #ec1f27;
    --grey: #9d9d9d;
    --grey-light: #b1b1b1;
    --white: #ffffff;
    --backdrop: #e9e7e3;
  }
  * { margin: 0; padding: 0; box-sizing: border-box; }
  html, body { width: 1200px; height: 900px; overflow: hidden; }
  body {
    background: var(--backdrop);
    font-family: "Quicksand", sans-serif;
    position: relative;
  }
  .card {
    position: absolute;
    left: 267px;
    width: 666px;
    height: 380px;
    overflow: hidden;
    box-shadow: 0 10px 28px rgba(0,0,0,.22);
  }

  /* Front: company name */
  .card-front {
    top: 50px;
    background: linear-gradient(135deg, var(--ink) 0%, var(--ink-soft) 100%);
  }
  .front-brand {
    position: absolute;
    left: 70px; top: 110px;
    display: flex; align-items: center; gap: 16px;
  }
  .brand-square {
    width: 46px; height: 46px;
    background: var(--orange);
  }
  .brand-name {
    color: var(--white);
    font-weight: 700;
    line-height: 1;
  }
  .brand-name .main { display: block; font-size: 44px; letter-spacing: 2px; }
  .brand-name .sub { display: block; font-size: 15px; letter-spacing: 3.3px; margin-top: 4px; }
  .front-band {
    position: absolute; left: 0; right: 0; bottom: 0;
    height: 40px;
    background: linear-gradient(90deg, var(--orange), var(--orange-light));
  }
  .front-band .grey-tab {
    position: absolute; right: 0; top: 0;
    width: 22%; height: 5px; background: var(--grey);
  }
  .front-band .web {
    position: absolute; right: 150px; top: 12px;
    color: var(--white); font-size: 14px; font-weight: 500;
  }
  .front-stripe {
    position: absolute; left: 0; bottom: 0;
    width: 78%; height: 5px;
    background: linear-gradient(90deg, var(--blue) 0 35%, var(--red) 35% 70%, var(--orange) 70% 100%);
  }

  /* Back: contact details */
  .card-back {
    top: 470px;
    background: linear-gradient(135deg, var(--ink) 0%, var(--ink-soft) 100%);
  }
  .back-top {
    position: absolute; left: 0; right: 0; top: 0;
    height: 205px;
    background: linear-gradient(90deg, var(--orange), var(--orange-light));
  }
  .back-stripe {
    position: absolute; left: 0; top: 200px;
    width: 100%; height: 6px;
    background: linear-gradient(90deg,
      var(--blue) 0 26%, var(--red) 26% 62%, var(--orange) 62% 84%, var(--grey) 84% 100%);
  }
  .back-square {
    position: absolute; left: 150px; top: 0;
    width: 140px; height: 118px;
    background: var(--ink);
  }
  .back-name {
    position: absolute; left: 150px; top: 128px;
    color: var(--ink);
    font-weight: 700; line-height: 1;
  }
  .back-name .main { display: block; font-size: 46px; letter-spacing: 2px; }
  .back-name .sub { display: block; font-size: 15px; letter-spacing: 3.6px; margin-top: 4px; }
  .address {
    position: absolute; left: 420px; top: 34px;
    display: flex; gap: 10px; align-items: flex-start;
    color: var(--white); font-size: 14px; font-weight: 500; line-height: 1.35;
  }
  .person {
    position: absolute; left: 200px; top: 290px;
    color: var(--orange); font-size: 18px; font-weight: 700;
  }
  .divider {
    position: absolute; left: 395px; top: 250px;
    width: 1px; height: 94px; background: var(--grey);
  }
  .contact-list {
    position: absolute; left: 415px; top: 244px;
    list-style: none;
    color: var(--white); font-size: 15px; font-weight: 500;
  }
  .contact-list li { display: flex; align-items: center; gap: 14px; height: 33px; }
  .icon { width: 20px; height: 20px; flex: none; }
</style>
</head>
<body>

  <section class="card card-front" aria-label="Business card front">
    <div class="front-brand">
      <span class="brand-square"></span>
      <span class="brand-name"><span class="main">VELMAR</span><span class="sub">CONSTRUCTION LLC</span></span>
    </div>
    <div class="front-band">
      <span class="grey-tab"></span>
      <span class="web">velmarllc.Com</span>
    </div>
    <div class="front-stripe"></div>
  </section>

  <section class="card card-back" aria-label="Business card back">
    <div class="back-top"></div>
    <div class="back-stripe"></div>
    <div class="back-square"></div>
    <div class="back-name"><span class="main">VELMAR</span><span class="sub">CONSTRUCTION LLC</span></div>

    <div class="address">
      <svg class="icon" viewBox="0 0 20 20" aria-hidden="true">
        <circle cx="10" cy="10" r="9.5" fill="#ffffff"/>
        <path d="M10 4.5a3.6 3.6 0 0 0-3.6 3.6c0 2.7 3.6 6.9 3.6 6.9s3.6-4.2 3.6-6.9A3.6 3.6 0 0 0 10 4.5z" fill="#f78f20"/>
        <circle cx="10" cy="8.1" r="1.3" fill="#ffffff"/>
      </svg>
      <span>418 harbor 87th.<br>Dunmoor park ny 10352</span>
    </div>

    <p class="person">Gerald tomasino</p>
    <div class="divider"></div>
    <ul class="contact-list">
      <li>
        <svg class="icon" viewBox="0 0 20 20" aria-hidden="true">
          <circle cx="10" cy="10" r="9.5" fill="#f78f20"/>
          <rect x="7" y="4.5" width="6" height="11" rx="1.2" fill="none" stroke="#1b1b1b" stroke-width="1.4"/>
          <circle cx="10" cy="13.3" r=".8" fill="#1b1b1b"/>
        </svg>
        <span>555-742-0583</span>
      </li>
      <li>
        <svg class="icon" viewBox="0 0 20 20" aria-hidden="true">
          <circle cx="10" cy="10" r="9.5" fill="#f78f20"/>
          <path d="M7 5.2l1.6-.4 1.1 2.6-1.1.9a6.5 6.5 0 0 0 3.1 3.1l.9-1.1 2.6 1.1-.4 1.6c-.2.6-.8.9-1.4.8A8.2 8.2 0 0 1 6.2 6.6c-.1-.6.2-1.2.8-1.4z" fill="#1b1b1b"/>
        </svg>
        <span>555-318-6094</span>
      </li>
      <li>
        <svg class="icon" viewBox="0 0 20 20" aria-hidden="true">
          <circle cx="10" cy="10" r="9.5" fill="#f78f20"/>
          <rect x="5" y="6.5" width="10" height="7" fill="#1b1b1b"/>
          <path d="M5 6.5l5 4 5-4" fill="none" stroke="#f78f20" stroke-width="1"/>
        </svg>
        <span>velmarllc@tridomail.Com</span>
      </li>
    </ul>
  </section>

</body>
</html>
```